Natural Sunscreen Label Design for a Natural Cosmetics brand

We are looking to create a label design for a Natural Sunscreen Lotion. The labels will be a stick-on label on a white background tube. Enclosed a file with the content and some ideas/references. Please feel free to explore more.

It is important that the SPF is highlighted as large text and to use colors that give the customer an impression this being a sunscreen from far away as well.
We like white and orange/amber/yellow.
Details attached
Our Logo is attached as well as the size template of the label.

```html
<!DOCTYPE html>
<html lang="en">
<head>
<meta charset="utf-8">
<title>Maresia Natural Sun Lotion Label</title>
<link href="https://fonts.googleapis.com/css2?family=Barlow+Condensed:wght@400;500;600;700&family=Barlow+Semi+Condensed:wght@300;400&display=swap" rel="stylesheet">
<style>
  :root {
    --bg: #ececec;
    --ink: #1f1f1f;
    --ink-soft: #3a3a3a;
    --orange: #e8792a;
    --orange-deep: #e0660f;
    --orange-light: #ea933d;
    --grey: #7a7a7a;
    --band: #8c8c8c;
    --white: #ffffff;
  }
  * { margin: 0; padding: 0; box-sizing: border-box; }
  html, body { width: 1200px; height: 1200px; overflow: hidden; }
  body {
    background: var(--bg);
    font-family: "Barlow Condensed", sans-serif;
    color: var(--ink);
    position: relative;
  }
  .row { position: absolute; left: 0; width: 1200px; text-align: center; }

  .brand { top: 120px; display: flex; flex-direction: column; align-items: center; gap: 18px; }
  .brand-dot { width: 110px; height: 110px; border: 5px solid var(--ink); border-radius: 50%; }
  .brand-name { font-weight: 500; font-size: 30px; letter-spacing: 8px; color: var(--ink); }

  .line-name { top: 376px; font-weight: 600; font-size: 36px; color: var(--orange); letter-spacing: 0.5px; }
  .product-en { top: 424px; font-weight: 600; font-size: 43px; color: var(--ink); }
  .product-pt { top: 474px; font-family: "Barlow Semi Condensed", sans-serif; font-weight: 400; font-size: 35px; color: var(--ink-soft); letter-spacing: 0.5px; }

  .spf { top: 530px; height: 200px; }
  .spf-value {
    position: absolute; left: 500px; top: 0;
    font-weight: 700; font-size: 214px; line-height: 1;
    background: linear-gradient(100deg, var(--orange-deep), var(--orange-light));
    -webkit-background-clip: text; background-clip: text; color: transparent;
  }
  .spf-label { position: absolute; left: 745px; top: 34px; font-weight: 600; font-size: 46px; color: var(--ink); }
  .spf-plus { position: absolute; left: 742px; top: 86px; }

  .uv { top: 780px; }
  .uv-box {
    display: inline-block; border: 2px solid var(--grey); color: var(--grey);
    font-family: "Barlow Semi Condensed", sans-serif; font-size: 26px; line-height: 1; padding: 5px 8px 4px;
  }
  .claims { top: 822px; font-family: "Barlow Semi Condensed", sans-serif; font-weight: 400; font-size: 30px; line-height: 34px; color: var(--ink-soft); }
  .claims .light { font-weight: 300; }

  .vegan { top: 946px; font-weight: 700; font-size: 38px; color: var(--grey); letter-spacing: 0.5px; }
  .usage { top: 998px; }
  .usage-band {
    display: inline-block; background: var(--band); color: var(--white);
    font-family: "Barlow Semi Condensed", sans-serif; font-weight: 400; font-size: 36px; line-height: 52px; padding: 0 12px; width: 313px;
  }
  .volume { top: 1074px; font-family: "Barlow Semi Condensed", sans-serif; font-size: 32px; color: var(--ink); }
</style>
</head>
<body>
  <div class="row brand">
    <div class="brand-dot"></div>
    <div class="brand-name">SOLMAR ORGANICS</div>
  </div>

  <div class="row line-name">MARESIA</div>
  <div class="row product-en">NATURAL SUN LOTION</div>
  <div class="row product-pt">LOÇÃO SOLAR NATURAL</div>

  <div class="row spf">
    <span class="spf-value">30</span>
    <span class="spf-label">SPF</span>
    <svg class="spf-plus" width="80" height="80" viewBox="0 0 80 80" aria-hidden="true">
      <defs>
        <linearGradient id="plus-fill" x1="0" y1="0" x2="1" y2="0">
          <stop offset="0" stop-color="#e8802e"/>
          <stop offset="1" stop-color="#ea933d"/>
        </linearGradient>
      </defs>
      <rect x="30" y="0" width="20" height="80" rx="2" fill="url(#plus-fill)"/>
      <rect x="0" y="30" width="80" height="20" rx="2" fill="url(#plus-fill)"/>
    </svg>
  </div>

  <div class="row uv"><span class="uv-box">UVA | UVB</span></div>
  <div class="row claims">
    <div><span class="light">With</span> BIO Aloe Vera | Non-greasy</div>
    <div>Water Resistant</div>
    <div class="light">Safe for kids and adults</div>
  </div>

  <div class="row vegan">VEGAN</div>
  <div class="row usage"><span class="usage-band">FOR BODY AND FACE</span></div>
  <div class="row volume">100ml</div>
</body>
</html>
```